Poster Required for Cafe to promote Catering

I would like a Poster made to advertise that our business does catering.
On the poster we would like it to say:

Did you know that Sunny Ladle does Catering?
We offer Breakfast, Lunch, Morning and Afternoon Tea Options
Come instore to enquire

At the bottom of the flyer, can you please put the contact details:
Phone 0487 602 914
Email tam@sunnyladlecanteen.com

Poster Size A3

I have attached our logo and menu's so you can get a feel for what we like.

Target Market(s)

Hospital Staff: Doctors, Nurses, Admin

Industry/Entity Type

Hospitality

Requirements
Nice to have
• Some pictures of catering. Eg. Gourmet Sandwiches, Sliders
• You could check our instagram page for ideas on what we do..
• @snyladle_qld

```html
<!DOCTYPE html>
<html lang="en">
<head>
<meta charset="utf-8">
<title>Sunny Ladle Catering Poster</title>
<link href="https://fonts.googleapis.com/css2?family=Cinzel:wght@400;700&family=Crimson+Text:wght@400&display=swap" rel="stylesheet">
<style>
  :root {
    --stage: #3a2418;
    --gold-light: #f4c46a;
    --amber: #b8741f;
    --bronze: #6a3c14;
    --espresso: #2a160c;
    --footer: #141010;
    --ink-dark: #17100b;
    --ink-light: #ffffff;
    --contact-gold: #e3b05a;
  }
  html, body {
    margin: 0;
    width: 1200px;
    height: 857px;
    overflow: hidden;
    background: var(--stage);
  }
  .poster {
    position: absolute;
    left: 341px;
    top: 28px;
    width: 518px;
    height: 800px;
    overflow: hidden;
    background: var(--espresso);
  }
  .hero-photo {
    position: absolute;
    inset: 0 0 130px 0;
    background:
      radial-gradient(ellipse 28% 60% at 50% 10%, rgba(255,236,190,0.55), transparent 70%),
      radial-gradient(ellipse 70% 22% at 62% 72%, rgba(230,225,220,0.22), transparent 75%),
      linear-gradient(180deg, var(--gold-light) 0%, var(--amber) 30%, var(--bronze) 55%, var(--espresso) 80%, #1a0e08 100%);
  }
  .brand-name {
    position: absolute;
    left: 0;
    top: 68px;
    width: 100%;
    margin: 0;
    text-align: center;
    font-family: "Crimson Text", serif;
    font-weight: 400;
    font-size: 32px;
    line-height: 1;
    color: var(--ink-dark);
  }
  .headline {
    position: absolute;
    left: 0;
    top: 0;
    width: 100%;
    text-align: center;
    font-family: "Cinzel", serif;
    font-size: 40px;
    letter-spacing: 1px;
    color: var(--ink-dark);
    line-height: 1;
    margin: 0;
    font-weight: 400;
  }
  .headline .line { position: absolute; left: 0; width: 100%; white-space: nowrap; }
  .headline strong { font-weight: 700; }
  .headline .highlight { color: var(--ink-light); font-weight: 700; }
  .offer {
    position: absolute;
    left: 0;
    top: 0;
    width: 100%;
    text-align: center;
    font-family: "Crimson Text", serif;
    color: var(--ink-light);
    text-shadow: 0 1px 3px rgba(0,0,0,0.6);
  }
  .offer .line { position: absolute; left: 0; width: 100%; white-space: nowrap; line-height: 1; margin: 0; }
  .offer .big { font-size: 41px; }
  .offer .small { font-size: 27px; }
  .contact-band {
    position: absolute;
    left: 0;
    bottom: 0;
    width: 100%;
    height: 130px;
    background: var(--footer);
    font-family: "Crimson Text", serif;
    font-variant-numeric: oldstyle-nums;
    color: var(--contact-gold);
    text-align: center;
  }
  .contact-phone {
    position: absolute; left: 0; width: 100%;
    top: 33px; font-size: 37px; line-height: 1; margin: 0;
  }
  .contact-email {
    position: absolute; left: 0; width: 100%;
    top: 75px; font-size: 24px; line-height: 1; margin: 0;
  }
</style>
</head>
<body>
  <main class="poster">
    <div class="hero-photo" role="img" aria-label="Steaming cup of coffee in warm golden light"></div>

    <p class="brand-name">Sunny Ladle</p>

    <h1 class="headline">
      <span class="line" style="top:170px">Did you know</span>
      <span class="line" style="top:223px">the <strong>Sunny</strong></span>
      <span class="line" style="top:277px">Ladle does</span>
      <span class="line highlight" style="top:330px">Catering?</span>
    </h1>

    <div class="offer">
      <p class="line" style="top:484px"><span class="small">We offer</span> <span class="big">Breakfast,</span></p>
      <p class="line" style="top:530px"><span class="big">Lunch &amp; Morning</span> <span class="small">&amp;</span></p>
      <p class="line" style="top:576px"><span class="big">Afternoon Tea</span> <span class="small">Options</span></p>
      <p class="line small" style="top:618px">Come instore to enquire</p>
    </div>

    <footer class="contact-band">
      <p class="contact-phone">Call Us Now 0487 602 914</p>
      <p class="contact-email">Email tam@sunnyladlecanteen.com</p>
    </footer>
  </main>
</body>
</html>
```